Law Offices business card

Hi there, I'll need business card for the Law Offices of Tobin Haskell. The information must convey his strategic approach and quick resolution to complex business litigation needs. Please emphasize Civil Litigation, Corporate Law, Business Governance and Real Estate Law. Tobin has over 25 years of experience in these fields.The card should be modern and edgy and the message should be clear. Please consult his current website for ideas.

Business

```html
<!DOCTYPE html>
<html lang="en">
<head>
<meta charset="utf-8">
<title>Law Offices of Tobin Haskell – Business Card</title>
<link rel="stylesheet" href="https://fonts.googleapis.com/css2?family=Jost:wght@300;400&family=Roboto+Condensed:wght@700&display=swap">
<style>
  :root {
    --backdrop-light: #e2e2e2;
    --backdrop-dark: #c9c9c9;
    --card: #1d1c1b;
    --ink-light: #e9e7e3;
    --ink-tan: #cbbba5;
    --ink-muted: #bdb4a8;
    --rule: #9e958a;
  }
  * { box-sizing: border-box; margin: 0; padding: 0; }
  html, body {
    width: 1200px;
    height: 849px;
    overflow: hidden;
  }
  body {
    background: radial-gradient(ellipse at 50% 40%, var(--backdrop-light), var(--backdrop-dark));
    position: relative;
    font-family: "Jost", sans-serif;
  }
  .card {
    position: absolute;
    top: 275px;
    width: 525px;
    height: 300px;
    background: var(--card);
    box-shadow: 0 14px 30px rgba(0, 0, 0, 0.25);
    overflow: hidden;
  }
  .card--front { left: 50px; }
  .card--back { left: 625px; }

  /* Front face */
  .front__rule {
    position: absolute;
    left: 0;
    right: 0;
    top: 92px;
    height: 1px;
    background: var(--rule);
  }
  .front__firm {
    position: absolute;
    right: 26px;
    top: 102px;
    font-family: "Roboto Condensed", sans-serif;
    font-weight: 700;
    font-size: 11px;
    letter-spacing: 0.06em;
    text-transform: uppercase;
    color: var(--ink-tan);
  }
  .front__services {
    position: absolute;
    left: 34px;
    bottom: 58px;
    list-style: none;
    font-weight: 300;
    font-size: 25px;
    line-height: 1.04;
    text-transform: uppercase;
    color: var(--ink-light);
  }
  .front__experience {
    position: absolute;
    left: 35px;
    bottom: 28px;
    font-family: "Roboto Condensed", sans-serif;
    font-weight: 700;
    font-size: 11px;
    letter-spacing: 0.06em;
    text-transform: uppercase;
    color: var(--ink-tan);
  }

  /* Back face */
  .back__frame {
    position: absolute;
    inset: 14px;
    border: 1px solid var(--rule);
  }
  .back__frame::after {
    content: "";
    position: absolute;
    inset: 3px;
    border: 1px solid var(--rule);
  }
  .back__content {
    position: absolute;
    left: 58px;
    top: 98px;
  }
  .back__name {
    font-family: "Roboto Condensed", sans-serif;
    font-weight: 700;
    font-size: 25px;
    letter-spacing: 0.04em;
    text-transform: uppercase;
    color: var(--ink-tan);
    line-height: 1;
  }
  .back__title {
    font-size: 10px;
    letter-spacing: 0.05em;
    margin-left: 4px;
  }
  .back__contact {
    margin-top: 10px;
    font-style: normal;
    font-weight: 300;
    font-size: 13.5px;
    line-height: 1.22;
    color: var(--ink-muted);
  }
  .sep { margin: 0 6px; }
</style>
</head>
<body>
  <section class="card card--front" aria-label="Card front">
    <div class="front__rule"></div>
    <p class="front__firm">Law Offices of Tobin Haskell, P.A.</p>
    <ul class="front__services">
      <li>Civil Litigation</li>
      <li>Corporate Law</li>
      <li>Business Governance</li>
      <li>Real Estate Law</li>
    </ul>
    <p class="front__experience">Over 25 years of experience</p>
  </section>

  <section class="card card--back" aria-label="Card back">
    <div class="back__frame"></div>
    <div class="back__content">
      <h1 class="back__name">Tobin Haskell<span class="back__title">Attorney</span></h1>
      <address class="back__contact">
        118B Lantana Avenue, Coral Point, Florida 33410<br>
        555-214-3090<span class="sep">|</span>555-214-3091<br>
        tobin@haskelllaw.com<span class="sep">|</span>www.haskelllaw.com
      </address>
    </div>
  </section>
</body>
</html>
```